Lumen Keyvault Password Manager WebApp Design

Lumen Keyvault is seeking an expert UI designer to provide a fresh and modern visual appeal for our product. Our inspiration comes from two major tools that have successfully managed to balance functionality and design aesthetics - Orbix Folder and Vaultmint. We want our application to exude a similar trustworthiness and modernity, through a clean, intuitive and responsive design.
We have established preliminary mockups and would like the designer to work within these parameters while enhancing the overall user experience. The primary tasks will involve innovative and improved designs of the login screen and the password screen, both being crucial touchpoints for our users. The login screen also serves a crucial role in demonstrating how our system works.
Key Elements:
Logo Integration: We are providing the logo for Lumen Keyvault. The design should align with the logo, both in terms of colors and overall aesthetic, to ensure a cohesive brand identity.
Color Palette: The UI design should adhere to the color palette derived from the logo to maintain brand consistency. The design should effectively utilize these colors to highlight important elements and improve user engagement.
Trustworthy and Modern Design: The UI should be professional and trustworthy. It should mirror the look and feel of Orbix Folder's simplicity and Vaultmint's solid security design, which inspires user confidence.
Adherence to Mockup Boundaries: The existing mockups serve as a guideline for the layout and placement of elements. The design should respect these boundaries while bringing innovation and visual appeal.
Improved Login Screen: The login screen is a key part of the user's journey and should be designed with utmost care. It should be intuitive, easy-to-use, visually engaging, and educative, showcasing how the system operates and encouraging users to sign in with confidence.
Enhanced Password Screen: The password screen, another key user touchpoint, needs improvement. The different types of passwords should be made more visible and intuitive, easing user interaction and enhancing the overall experience.
Prospective designers are encouraged to test our current version available for free at app.lumenkeyvault.com to understand the product better and contribute to meaningful design enhancements.
The goal of this project is to provide a visually compelling and user-friendly interface for Lumen Keyvault that inspires user trust, while adhering to the branding elements, including color scheme and logo design. The ideal designer will have a proven track record of creating compelling UI designs that enhance user experience and engagement.
We preferred the design to be in Figma.
Please provide the 3 design so we can evaluate if we like to choice you:
1. Login Page.
2. Passwords View design
3. Single Passwod Page
We need all the pages to be design that are provided as screenshots.

```html
<!DOCTYPE html>
<html lang="en">
<head>
<meta charset="utf-8">
<title>Lumen Keyvault – Last Used</title>
<link href="https://fonts.googleapis.com/css2?family=Inter:wght@400;500;600;700&display=swap" rel="stylesheet">
<style>
:root{
  --rail-bg:#eef1f5;
  --app-bg:#f6f7f9;
  --panel:#ffffff;
  --ink:#1f2328;
  --ink-soft:#3d4248;
  --muted:#8a9096;
  --line:#d9dce0;
  --brand:#3f6fc6;
  --brand-soft:#dde8f8;
  --amber-bg:#fdf1d6;
  --amber:#e2861b;
  --violet-bg:#ebe8fb;
  --violet:#6b5bd2;
  --avatar:#7a5a48;
}
*{box-sizing:border-box;margin:0;padding:0}
html,body{width:1200px;height:779px;overflow:hidden}
body{font-family:"Inter",sans-serif;background:var(--app-bg);color:var(--ink);position:relative}

.rail{position:absolute;left:0;top:0;width:48px;height:779px;background:var(--rail-bg)}
.rail-btn{position:absolute;left:8px;width:32px;height:32px;display:flex;align-items:center;justify-content:center;border-radius:7px;color:var(--ink-soft)}
.rail-btn.active{background:var(--brand-soft);color:var(--brand)}
.rail-indicator{position:absolute;left:47px;top:71px;width:2px;height:32px;background:var(--brand);border-radius:1px}
.avatar{position:absolute;left:10px;top:738px;width:28px;height:28px;border-radius:50%;background:radial-gradient(circle at 50% 40%,#b48a6e,var(--avatar));border:2px solid #fff}

.sidebar{position:absolute;left:48px;top:0;width:272px;height:779px}
.brand{position:absolute;left:16px;top:27px;display:flex;align-items:center;gap:10px;font-size:16px;font-weight:500;color:var(--ink)}
.brand-mark{width:20px;height:20px;border-radius:4px;background:var(--brand)}
.nav-item{position:absolute;left:0;display:flex;align-items:center;font-size:13px;color:var(--ink);height:20px;transform:translateY(-50%)}
.nav-item .chev{position:absolute;left:14px;width:10px;height:10px;color:var(--ink)}
.nav-item .ico{position:absolute;left:39px;width:18px;height:18px;color:var(--ink-soft)}
.nav-item .label{position:absolute;left:71px;white-space:nowrap}
.nav-item.open .label{font-weight:600}
.nav-sub{position:absolute;left:71px;font-size:13px;color:var(--ink-soft);transform:translateY(-50%);white-space:nowrap}
.create-btn{position:absolute;left:12px;top:603px;width:175px;height:38px;background:#fff;border-radius:7px;display:flex;align-items:center;gap:8px;padding-left:14px;font-size:13px;color:var(--ink)}

.page-title{position:absolute;left:333px;top:43px;font-size:19px;font-weight:600;letter-spacing:-0.3px}
.search{position:absolute;left:919px;top:37px;width:266px;height:32px;border:1px solid var(--line);border-radius:5px;background:#fff;display:flex;align-items:center;gap:8px;padding-left:10px;font-size:13px;color:var(--muted)}

.panel{position:absolute;left:333px;top:82px;width:852px;height:686px;background:var(--panel);border-radius:16px;padding:20px 17px}
.grid{display:grid;grid-template-columns:repeat(4,194px);column-gap:13.6px;row-gap:13px}
.card{height:58px;border:1px solid var(--line);border-radius:8px;display:flex;align-items:center;gap:12px;padding-left:10px;font-size:13px;font-weight:500}
.card-icon{width:35px;height:35px;border-radius:8px;background:var(--amber-bg);color:var(--amber);display:flex;align-items:center;justify-content:center}
.card-icon.mail{background:var(--violet-bg);color:var(--violet)}
</style>
</head>
<body>

<aside class="rail">
  <div class="rail-btn active" style="top:71px">
    <svg width="16" height="16" viewBox="0 0 16 16" fill="none" stroke="currentColor" stroke-width="1.4"><path d="M2.5 7L8 2.5 13.5 7v6.5h-4v-4h-3v4h-4z" stroke-linejoin="round"/></svg>
  </div>
  <div class="rail-indicator"></div>
  <div class="rail-btn" style="top:123px">
    <svg width="18" height="14" viewBox="0 0 18 14" fill="currentColor"><circle cx="9" cy="4" r="2.2"/><circle cx="4" cy="5.5" r="1.7"/><circle cx="14" cy="5.5" r="1.7"/><path d="M5.5 12a3.5 3.5 0 017 0z"/><path d="M1 12a3 3 0 014-2.8V12zM17 12a3 3 0 00-4-2.8V12z"/></svg>
  </div>
  <div class="rail-btn" style="top:173px">
    <svg width="16" height="16" viewBox="0 0 16 16" fill="none" stroke="currentColor" stroke-width="1.4"><path d="M4 11V7a4 4 0 018 0v4l1 1.5H3z" stroke-linejoin="round"/><path d="M6.5 14h3"/></svg>
  </div>
  <div class="rail-btn" style="top:224px">
    <svg width="16" height="16" viewBox="0 0 16 16" stroke="currentColor" stroke-width="1.4"><path d="M2 4h12M2 8h12M2 12h12"/></svg>
  </div>
  <div class="avatar" role="img" aria-label="User profile photo"></div>
</aside>

<nav class="sidebar">
  <div class="brand"><span class="brand-mark"></span><span>Lumen Keyvault</span></div>

  <div class="nav-item" style="top:88px">
    <svg class="chev" viewBox="0 0 10 10" fill="none" stroke="currentColor" stroke-width="1.4"><path d="M3.5 1.5L7 5 3.5 8.5"/></svg>
    <svg class="ico" viewBox="0 0 18 18" fill="none" stroke="currentColor" stroke-width="1.4"><rect x="2" y="2" width="5" height="7"/><rect x="10" y="2" width="5" height="4"/><rect x="2" y="12" width="5" height="4"/><rect x="10" y="9" width="5" height="7"/></svg>
    <span class="label" style="left:68px">General</span>
  </div>
  <div class="nav-item" style="top:141px">
    <svg class="chev" viewBox="0 0 10 10" fill="none" stroke="currentColor" stroke-width="1.4"><path d="M3.5 1.5L7 5 3.5 8.5"/></svg>
    <svg class="ico" viewBox="0 0 18 18" fill="none" stroke="currentColor" stroke-width="1.4"><path d="M2 4h5l1.5 2H16v9H2z" stroke-linejoin="round"/><circle cx="12" cy="10" r="1.3"/><path d="M10 13.5a2 2 0 014 0"/></svg>
    <span class="label">Shared with Me</span>
  </div>
  <div class="nav-item open" style="top:194px">
    <svg class="chev" viewBox="0 0 10 10" fill="none" stroke="currentColor" stroke-width="1.4"><path d="M1.5 3.5L5 7 8.5 3.5"/></svg>
    <svg class="ico" viewBox="0 0 18 18"><rect x="1" y="5" width="16" height="11" rx="1.5" fill="var(--brand)"/><path d="M6 5V3h6v2" fill="none" stroke="var(--brand)" stroke-width="1.5"/></svg>
    <span class="label">Work</span>
  </div>
  <div class="nav-sub" style="top:224px">Import-KI-Password-8.03.23</div>
  <div class="nav-sub" style="top:263px">Import-KI-Password-8.03.23</div>
  <div class="nav-sub" style="top:302px">Import-KI-Password-8.03.23</div>
  <div class="nav-item" style="top:358px">
    <svg class="chev" viewBox="0 0 10 10" fill="none" stroke="currentColor" stroke-width="1.4"><path d="M3.5 1.5L7 5 3.5 8.5"/></svg>
    <svg class="ico" viewBox="0 0 18 18" fill="none" stroke="currentColor" stroke-width="1.3"><circle cx="9" cy="4" r="2"/><circle cx="3.5" cy="13" r="2"/><circle cx="14.5" cy="13" r="2"/><path d="M7.5 5.5L4.5 11M10.5 5.5l3 5.5M5.5 13.5h7"/></svg>
    <span class="label">Social Media</span>
  </div>
  <div class="nav-item" style="top:408px">
    <svg class="chev" viewBox="0 0 10 10" fill="none" stroke="currentColor" stroke-width="1.4"><path d="M3.5 1.5L7 5 3.5 8.5"/></svg>
    <svg class="ico" viewBox="0 0 18 18" fill="none" stroke="currentColor" stroke-width="1.4"><path d="M1.5 2.5h2.5l2 9h8.5l1.5-6.5H5" stroke-linejoin="round"/><circle cx="7" cy="15" r="1.2"/><circle cx="13.5" cy="15" r="1.2"/></svg>
    <span class="label">Shopping</span>
  </div>
  <div class="nav-item" style="top:459px">
    <svg class="chev" viewBox="0 0 10 10" fill="none" stroke="currentColor" stroke-width="1.4"><path d="M3.5 1.5L7 5 3.5 8.5"/></svg>
    <svg class="ico" viewBox="0 0 18 18" fill="none" stroke="currentColor" stroke-width="1.4"><path d="M2 4l4.5-1.5 5 1.5L16 2.5v11.5L11.5 15.5l-5-1.5L2 15.5z M6.5 2.5V14 M11.5 4v11.5" stroke-linejoin="round"/></svg>
    <span class="label">Travel</span>
  </div>
  <div class="nav-item" style="top:510px">
    <svg class="chev" viewBox="0 0 10 10" fill="none" stroke="currentColor" stroke-width="1.4"><path d="M3.5 1.5L7 5 3.5 8.5"/></svg>
    <svg class="ico" viewBox="0 0 18 18" fill="none" stroke="currentColor" stroke-width="1.3"><path d="M2 6l7-4 7 4zM2 16h14M4 8v6M7.3 8v6M10.7 8v6M14 8v6"/></svg>
    <span class="label">Banking</span>
  </div>
  <div class="nav-item" style="top:560px">
    <svg class="chev" viewBox="0 0 10 10" fill="none" stroke="currentColor" stroke-width="1.4"><path d="M3.5 1.5L7 5 3.5 8.5"/></svg>
    <svg class="ico" viewBox="0 0 18 18" fill="none" stroke="currentColor" stroke-width="1.3"><path d="M2 7l7-5 7 5v8H2z" stroke-linejoin="round"/><path d="M2 7l7 4.5L16 7M4.5 5.5V4h9v1.5"/></svg>
    <span class="label" style="left:73px">Emails</span>
  </div>

  <div class="create-btn">
    <svg width="12" height="12" viewBox="0 0 12 12" stroke="var(--brand)" stroke-width="1.5"><path d="M6 0v12M0 6h12"/></svg>
    <span>Create Main Category</span>
  </div>
</nav>

<h1 class="page-title">Last Used</h1>
<div class="search">
  <svg width="15" height="15" viewBox="0 0 15 15" fill="none" stroke="var(--muted)" stroke-width="1.5"><circle cx="6" cy="6" r="4.8"/><path d="M9.5 9.5l4.5 4.5"/></svg>
  <span>Search</span>
</div>

<main class="panel">
  <div class="grid">
    <div class="card"><span class="card-icon"><svg width="16" height="16" viewBox="0 0 16 16" fill="none" stroke="currentColor" stroke-width="1.4"><rect x="2" y="2" width="12" height="12" rx="1"/><path d="M5.5 5h5"/></svg></span>Test 232</div>
    <div class="card"><span class="card-icon"><svg width="16" height="16" viewBox="0 0 16 16" fill="none" stroke="currentColor" stroke-width="1.4"><rect x="2" y="2" width="12" height="12" rx="1"/><path d="M5.5 5h5"/></svg></span>Test 232</div>
    <div class="card"><span class="card-icon"><svg width="16" height="16" viewBox="0 0 16 16" fill="none" stroke="currentColor" stroke-width="1.4"><rect x="2" y="2" width="12" height="12" rx="1"/><path d="M5.5 5h5"/></svg></span>Test 232</div>
    <div class="card"><span class="card-icon"><svg width="16" height="16" viewBox="0 0 16 16" fill="none" stroke="currentColor" stroke-width="1.4"><rect x="2" y="2" width="12" height="12" rx="1"/><path d="M5.5 5h5"/></svg></span>Test 232</div>
    <div class="card"><span class="card-icon"><svg width="16" height="16" viewBox="0 0 16 16" fill="none" stroke="currentColor" stroke-width="1.4"><rect x="2" y="2" width="12" height="12" rx="1"/><path d="M5.5 5h5"/></svg></span>Test 232</div>
    <div class="card"><span class="card-icon mail"><svg width="16" height="16" viewBox="0 0 16 16" fill="none" stroke="currentColor" stroke-width="1.3"><path d="M1.5 6.5L8 2l6.5 4.5v7.5h-13z" stroke-linejoin="round"/><path d="M1.5 6.5L8 10.5l6.5-4M4 5V3.5h8V5"/></svg></span>Test 232</div>
    <div class="card"><span class="card-icon"><svg width="16" height="16" viewBox="0 0 16 16" fill="none" stroke="currentColor" stroke-width="1.4"><rect x="2" y="2" width="12" height="12" rx="1"/><path d="M5.5 5h5"/></svg></span>Test 232</div>
    <div class="card"><span class="card-icon"><svg width="16" height="16" viewBox="0 0 16 16" fill="none" stroke="currentColor" stroke-width="1.4"><rect x="2" y="2" width="12" height="12" rx="1"/><path d="M5.5 5h5"/></svg></span>Test 232</div>
  </div>
</main>

</body>
</html>
```